Hispanic Financial Counseling and Advocate Firm seeks business card design

Looking for a clean, professional business card design. This is a firm that specializes in providing financial education, coaching, and planning to the Hispanic community. The name of the company is Valemar, which means to prosper. We need a design that is clean, professional, and invokes trust, professionalism, but also welcoming. Our logo is a plant growing from a hand to give the messaging of of being in control of growing your financial future and security. Its part of a larger organization names Celesta Financial Group, who's logo is a tree with multi colored branches. We have the back of the card designed so we just need the front designed. the back is blue, so front needs to be a different background color, not blue.

Target Market(s)

Hispanic Community looking to better their future

Industry/Entity Type

financial services

Contact Information for Business Card

contact info: Anselmo Ibarra Jr, 951-555-0147, info@celestafinancialgroup.example. Celestafinancialgroup.example. tag line: Para un futuro mas seguro!

Requirements
Must have
• basics: logo, contact info.
Nice to have
• possibly incorporate the tree logo provided somehow
Should not have
• should not look like the back, needs to be different from the back provided.

```html
<!DOCTYPE html>
<html lang="es">
<head>
<meta charset="utf-8">
<title>Valemar – Tarjeta de presentación</title>
<link rel="stylesheet" href="https://fonts.googleapis.com/css2?family=Nunito:wght@700;800&family=Open+Sans:wght@400;600&display=swap">
<style>
  :root {
    --backdrop: #e4e6e8;
    --card: #ffffff;
    --card-shade: #eceeef;
    --green: #5aa83c;
    --green-faint: #e9f1e4;
    --navy: #3f4d6b;
    --ink: #4a4f57;
  }
  * { box-sizing: border-box; margin: 0; padding: 0; }
  html, body { width: 1200px; height: 900px; overflow: hidden; }
  body {
    background: var(--backdrop);
    display: flex; align-items: center; justify-content: center;
  }
  .business-card {
    position: relative;
    width: 1000px; height: 572px;
    overflow: hidden;
    background: linear-gradient(120deg, var(--card-shade) 0%, var(--card) 45%, var(--card) 100%);
    box-shadow: 0 14px 40px rgba(0,0,0,.18);
    font-family: "Open Sans", sans-serif;
  }
  .backdrop-accent {
    position: absolute; left: 90px; top: 150px;
    width: 380px; height: 380px; border-radius: 50%;
    background: radial-gradient(circle, var(--green-faint) 0%, rgba(233,241,228,.5) 60%, rgba(233,241,228,0) 100%);
  }
  .brand {
    position: absolute; right: 70px; top: 40px;
    width: 400px;
    display: flex; flex-direction: column; align-items: center;
    text-align: center;
  }
  .brand-mark {
    width: 96px; height: 96px; border-radius: 50%;
    background: var(--green);
    margin-bottom: 14px;
  }
  .brand-name {
    font-family: "Nunito", sans-serif; font-weight: 700;
    font-size: 86px; line-height: 1; color: var(--green);
    letter-spacing: -1px;
  }
  .brand-descriptor {
    margin-top: 10px;
    font-family: "Nunito", sans-serif; font-weight: 800;
    font-size: 21px; letter-spacing: 2px; color: var(--navy);
  }
  .brand-tagline {
    margin-top: 4px;
    font-size: 20px; color: var(--green); letter-spacing: .5px;
  }
  .holder-name {
    position: absolute; left: 150px; top: 300px;
    font-family: "Nunito", sans-serif; font-weight: 700;
    font-size: 40px; color: var(--green);
  }
  .contact {
    position: absolute; display: flex; align-items: center; gap: 12px;
    font-size: 26px; color: var(--ink);
  }
  .contact svg { width: 24px; height: 24px; fill: var(--navy); flex: none; }
  .contact-phone { left: 230px; top: 408px; }
  .contact-email { right: 70px; top: 408px; }
  .contact-web { left: 230px; top: 476px; }
  .divider {
    position: absolute; left: 220px; right: 60px; top: 458px;
    height: 2px; background: var(--green);
  }
</style>
</head>
<body>
  <article class="business-card">
    <div class="backdrop-accent" role="img" aria-label="Faint decorative area in pale green"></div>

    <header class="brand">
      <div class="brand-mark" aria-hidden="true"></div>
      <div class="brand-name">Valemar</div>
      <div class="brand-descriptor">SERVICIOS FINANCIEROS</div>
      <div class="brand-tagline">Para un futuro mas seguro!</div>
    </header>

    <h1 class="holder-name">Anselmo Ibarra Jr</h1>

    <div class="contact contact-phone">
      <svg viewBox="0 0 24 24" aria-hidden="true"><path d="M2 9c0-3 5-5 10-5s10 2 10 5v2h-5V9c-1-1-3-1.5-5-1.5S8 8 7 9v2H2z"/><path d="M6 12h12l2 8H4z"/></svg>
      <span>951-555-0147</span>
    </div>

    <div class="contact contact-email">
      <svg viewBox="0 0 24 24" aria-hidden="true"><path d="M2 9l10-6 10 6v11H2z"/><path d="M4 10l8 5 8-5" fill="none" stroke="#fff" stroke-width="1.6"/></svg>
      <span>info@celestafinancialgroup.example</span>
    </div>

    <div class="divider"></div>

    <div class="contact contact-web">
      <svg viewBox="0 0 24 24" aria-hidden="true"><circle cx="12" cy="12" r="10"/><path d="M2 12h20M12 2c3 3 3 17 0 20M12 2c-3 3-3 17 0 20" fill="none" stroke="#fff" stroke-width="1.4"/></svg>
      <span>Celestafinancialgroup.example</span>
    </div>
  </article>
</body>
</html>
```